I need the Scorecard I've developed for my staff to be produced into a visually engaging piece that will encourage the staff to utilize it on a daily basis. I'm thinking it could be 5x7 in size so that it isn't too cumbersome, but I'm open to different layouts.
I have multiple other departments that will need Scorecards created for them as well, but each one will contain task specific questions for each department.

```html
<!DOCTYPE html>
<html lang="en">
<head>
<meta charset="UTF-8">
<title>Receptionist Daily Excellence Scorecard</title>
<link href="https://fonts.googleapis.com/css2?family=Arimo:wght@400;700&family=Roboto+Condensed:wght@400&display=swap" rel="stylesheet">
<style>
:root{
  --frame:#d8262b;
  --title:#0b4f9c;
  --band:#5f5b59;
  --blue-h:#8fcdf0; --blue-r:#cfe6f8;
  --gold-h:#e5cd7e; --gold-r:#fbe9a3;
  --lilac-h:#c3bbdc; --lilac-r:#e3dfef;
  --rose-h:#e096ae; --rose-r:#f9d5e2;
  --lime-h:#a9d05f; --lime-r:#d3e7a0;
  --peach-h:#ecc19d; --peach-r:#f3dcc5;
  --grey-r:#dedede; --slate-r:#d4dce1;
  --mint-h:#82c19d; --mint-r:#c8e5d3;
  --orange-h:#eea152; --orange-r:#f4d2a8;
  --plum-r:#dfc9e0;
  --ink:#1f1f1f;
  --red:#e0262c; --sky:#1aa0dc; --green:#1a9a3a;
}
*{box-sizing:border-box;margin:0;padding:0}
html,body{width:1200px;height:960px;overflow:hidden;background:#fff}
body{font-family:"Arimo",Arial,sans-serif;color:var(--ink);position:relative}
.frame{position:absolute;left:25px;top:21px;width:1147px;height:917px;border:2px solid var(--frame)}
.portrait{position:absolute;left:50px;top:39px;width:99px;height:130px;border-radius:6px;background:linear-gradient(180deg,#d9d9d9,#bdb7b2);box-shadow:2px 3px 5px rgba(0,0,0,.25);border:3px solid #fff}
.title{position:absolute;left:171px;top:34px;font-size:40.5px;color:var(--title);letter-spacing:.2px;white-space:nowrap}
.field{position:absolute;border:1.5px solid #8a8a8a;font-size:19px;padding-left:9px;display:flex;align-items:center}
.field.name{left:175px;top:89px;width:543px;height:36px}
.field.loc{left:175px;top:135px;width:543px;height:35px}
.field.loc span.date{position:absolute;left:318px}
.rate-box{position:absolute;left:744px;top:89px;width:407px;height:81px;border:1.5px solid #8a8a8a;font-family:"Roboto Condensed",sans-serif;text-align:center}
.rate-box .ask{font-size:21px;margin-top:12px}
.rate-box .scale{font-size:17.5px;margin-top:6px;display:flex;justify-content:center;gap:8px}
.r1{color:var(--red)}.r3{color:var(--sky)}.r5{color:var(--green)}
.divider{position:absolute;left:600px;top:192px;height:730px;border-left:1px dashed #999}
.sec{position:absolute;width:529px}
.sec-head{height:26px;background:var(--band);border-radius:13px 13px 0 0;color:#fff;font-weight:700;font-size:17px;display:flex;align-items:center;justify-content:center;position:relative}
.sec-head .icon{position:absolute;top:-11px}
.grid{display:grid;grid-template-columns:289px 112px 128px;gap:2px;background:#fff;margin-top:2px}
.grid .th{height:25px;display:flex;align-items:center;font-family:"Roboto Condensed",sans-serif;font-size:17px;justify-content:center}
.grid .th.task{justify-content:flex-start;padding-left:12px;font-family:"Arimo",sans-serif;font-size:16px}
.grid .td{height:26px;display:flex;align-items:center;padding-left:12px;font-size:14.5px}
.call .grid .td{font-size:13px}
.call .th{background:var(--blue-h)} .call .td{background:var(--blue-r)}
.busy .th{background:var(--gold-h)} .busy .td{background:var(--gold-r)}
.sched .th{background:var(--lilac-h)} .sched .td{background:var(--lilac-r)}
.cloth .th{background:var(--rose-h)} .cloth .td{background:var(--rose-r)}
.dc .th{background:var(--lime-h)} .dc .td{background:var(--lime-r)}
.route .th{background:var(--peach-h)} .route .td{background:var(--peach-r)}
.rows{display:flex;flex-direction:column;gap:2px;margin-top:2px}
.status .row{height:25.5px;background:var(--grey-r);display:flex;align-items:center;font-size:14.5px}
.status .row:last-child{background:var(--slate-r)}
.status .dot{width:12px;height:12px;border-radius:50%;background:#fff;margin:0 14px 0 11px}
.status .lbl{width:114px}
.line-row{height:26px;display:flex;align-items:center;padding-left:16px;font-size:14.5px}
.line-row .fill{flex:1;border-bottom:1px dotted #666;margin:0 6px 0 6px;height:14px}
.reflect .line-row{background:var(--mint-r)}
.reflect .sec-head{background:var(--mint-h);border-radius:13px 13px 0 0;font-size:17.5px}
.flags .sec-head{background:var(--orange-h);font-size:17.5px}
.flags .line-row{background:var(--orange-r);padding-left:10px}
.flags .line-row svg{margin-right:4px}
.mgr{width:293px}
.mgr .line-row{background:var(--plum-r);font-family:"Roboto Condensed",sans-serif;font-size:15.5px;padding-left:12px}
.sign{position:absolute;left:927px;top:837px;width:224px;height:82px;border:1.5px solid #999;border-radius:8px;font-family:"Roboto Condensed",sans-serif;font-size:15.5px;padding:10px 6px 0 10px}
.sign .s{display:flex;height:24px;align-items:center}
.sign .s .fill{flex:1;border-bottom:1px dotted #666;height:12px;margin-left:3px}
.sign .s.d{padding-left:72px}
</style>
</head>
<body>
<div class="frame"></div>
<div class="portrait" role="img" aria-label="Staff member portrait photo"></div>
<h1 class="title">RECEPTIONIST DAILY EXCELLENCE SCORECARD</h1>
<div class="field name">Name :</div>
<div class="field loc">Location :<span class="date">Date :</span></div>
<div class="rate-box">
  <div class="ask">Please Rate yourself for each task</div>
  <div class="scale"><span class="r1">1 = Needs Improvement</span><span class="r3">3 = Meets Expectations</span><span class="r5">5 = Excellent</span></div>
</div>
<div class="divider"></div>

<section class="sec call" style="left:48px;top:190px">
  <div class="sec-head">
    <svg class="icon" style="left:42px;top:-10px" width="28" height="32" viewBox="0 0 28 32"><rect x="2" y="4" width="22" height="26" fill="#3b2f8f"/><g stroke="#fff" stroke-width="1.5"><line x1="6" y1="12" x2="18" y2="12"/><line x1="6" y1="17" x2="16" y2="17"/><line x1="6" y1="22" x2="13" y2="22"/></g><g fill="#3b2f8f"><rect x="4" y="0" width="2" height="5"/><rect x="9" y="0" width="2" height="5"/><rect x="14" y="0" width="2" height="5"/><rect x="19" y="0" width="2" height="5"/></g><path d="M14 26l10-12 3 2-10 12-4 1z" fill="#3b2f8f" stroke="#fff"/></svg>
    1. Call Handling &amp; First Call Intake</div>
  <div class="grid">
    <div class="th task">Task</div><div class="th">Self-Rating (1-5)</div><div class="th">Notes / Issues</div>
    <div class="td">Answered 90%+ calls within 3 rings</div><div class="td"></div><div class="td"></div>
    <div class="td">Maintained empathy and professionalism</div><div class="td"></div><div class="td"></div>
    <div class="td">Accurately completed all First Call fields</div><div class="td"></div><div class="td"></div>
    <div class="td">Worked within Receptionist role</div><div class="td"></div><div class="td"></div>
  </div>
</section>

<section class="sec busy" style="left:48px;top:371px">
  <div class="sec-head">
    <svg class="icon" style="left:44px;top:-10px" width="18" height="28" viewBox="0 0 18 28"><path d="M3 2c3-2 6 0 6 3l-2 4c-1 2 0 6 3 10l3-1c2 0 3 2 3 4l-2 4c-6 2-14-12-13-20z" fill="#f07f1b"/></svg>
    2. Call Management During Busy Times</div>
  <div class="grid">
    <div class="th task">Task</div><div class="th">Self-Rating (1-5)</div><div class="th">Notes / Issues</div>
    <div class="td">Prioritized urgent vs. non-urgent calls</div><div class="td"></div><div class="td"></div>
    <div class="td">Hold times under 1 minute</div><div class="td"></div><div class="td"></div>
    <div class="td">Logged all calls</div><div class="td"></div><div class="td"></div>
    <div class="td">Requested help if overwhelmed</div><div class="td"></div><div class="td"></div>
  </div>
</section>

<section class="sec sched" style="left:48px;top:548px">
  <div class="sec-head">
    <svg class="icon" style="left:61px;top:-10px" width="34" height="32" viewBox="0 0 34 32"><rect x="1" y="4" width="32" height="27" fill="#3b3c8f"/><rect x="3" y="10" width="28" height="19" fill="#fff"/><g fill="#3b3c8f"><rect x="5" y="12" width="5" height="4"/><rect x="12" y="12" width="5" height="4"/><rect x="19" y="12" width="5" height="4"/><rect x="26" y="12" width="4" height="4"/><rect x="5" y="18" width="5" height="4"/><rect x="12" y="18" width="5" height="4"/><rect x="19" y="18" width="5" height="4"/><rect x="26" y="18" width="4" height="4"/><rect x="5" y="24" width="5" height="4"/><rect x="12" y="24" width="5" height="4"/><rect x="19" y="24" width="5" height="4"/><rect x="7" y="0" width="3" height="7"/><rect x="24" y="0" width="3" height="7"/></g></svg>
    3. Scheduling Accuracy</div>
  <div class="grid">
    <div class="th task">Task</div><div class="th">Self-Rating (1-5)</div><div class="th">Notes / Issues</div>
    <div class="td">Updated scheduling board</div><div class="td"></div><div class="td"></div>
    <div class="td">Cross-checked with Red Book</div><div class="td"></div><div class="td"></div>
    <div class="td">Entered manifold info promptly</div><div class="td"></div><div class="td"></div>
  </div>
</section>

<section class="sec cloth" style="left:48px;top:698px">
  <div class="sec-head">
    <svg class="icon" style="left:76px;top:-10px" width="34" height="34" viewBox="0 0 34 34"><path d="M11 1l6 3 6-3 10 7-4 7-4-2v20H9V13l-4 2-4-7z" fill="#e0157a"/></svg>
    4. Clothing &amp; Flowers</div>
  <div class="grid">
    <div class="th task">Task</div><div class="th">Self-Rating (1-5)</div><div class="th">Notes / Issues</div>
    <div class="td">Clothing sheet completed</div><div class="td"></div><div class="td"></div>
    <div class="td">Family contact noted on sheet</div><div class="td"></div><div class="td"></div>
    <div class="td">Floral deliveries logged</div><div class="td"></div><div class="td"></div>
    <div class="td">Concerns communicated to</div><div class="td"></div><div class="td"></div>
    <div class="td">Care Center</div><div class="td"></div><div class="td"></div>
    <div class="td">Flower placement verified</div><div class="td"></div><div class="td"></div>
  </div>
</section>

<section class="sec dc" style="left:622px;top:190px">
  <div class="sec-head">
    <svg class="icon" style="left:126px;top:-13px" width="32" height="34" viewBox="0 0 32 34"><rect x="3" y="2" width="26" height="30" fill="#fff" stroke="#2e9b5a" stroke-width="2"/><g stroke="#2e9b5a" stroke-width="1.5"><line x1="8" y1="8" x2="24" y2="8"/><line x1="14" y1="14" x2="24" y2="14"/><line x1="14" y1="19" x2="24" y2="19"/><line x1="14" y1="24" x2="24" y2="24"/></g><circle cx="9" cy="17" r="3.5" fill="none" stroke="#2e9b5a" stroke-width="1.5"/><path d="M7 20l-1 6 3-2 3 2-1-6" fill="none" stroke="#2e9b5a" stroke-width="1.5"/></svg>
    5. Death Certificates</div>
  <div class="grid">
    <div class="th task">Task</div><div class="th">Self-Rating (1-5)</div><div class="th">Notes / Issues</div>
    <div class="td">Verified recipient ID&amp; relationship</div><div class="td"></div><div class="td"></div>
    <div class="td">Confirmed correct documents enclosed</div><div class="td"></div><div class="td"></div>
    <div class="td">Recipient signed the DC logbook</div><div class="td"></div><div class="td"></div>
    <div class="td">Suggested proofreading before leaving</div><div class="td"></div><div class="td"></div>
  </div>
</section>

<section class="sec route" style="left:622px;top:363px">
  <div class="sec-head">
    <svg class="icon" style="left:100px;top:-6px" width="34" height="30" viewBox="0 0 34 30"><ellipse cx="17" cy="13" rx="16" ry="12" fill="#e58a45"/><path d="M5 20l-2 9 9-5z" fill="#e58a45"/><g fill="#fff"><circle cx="10" cy="13" r="2"/><circle cx="17" cy="13" r="2"/><circle cx="24" cy="13" r="2"/></g></svg>
    6. Routing &amp; Messages</div>
  <div class="grid">
    <div class="th task">Task</div><div class="th">Self-Rating (1-5)</div><div class="th">Notes / Issues</div>
    <div class="td">Calls routed appropriately</div><div class="td"></div><div class="td"></div>
    <div class="td">Messages included all required info</div><div class="td"></div><div class="td"></div>
    <div class="td">Delivered 95%+ messages in 30 min</div><div class="td"></div><div class="td"></div>
  </div>
</section>

<section class="sec status" style="left:622px;top:507px">
  <div class="sec-head">
    <svg width="22" height="20" viewBox="0 0 22 20" style="margin-right:12px"><path d="M2 11l6 7L20 2" fill="none" stroke="#fff" stroke-width="2"/></svg>
    Daily Status Summary (Tick One)</div>
  <div class="rows">
    <div class="row"><span class="dot"></span><span class="lbl">Excellent</span>All key duties completed, proactive, calm under pressure</div>
    <div class="row"><span class="dot"></span><span class="lbl">Satisfactory</span>Most duties completed, minor follow-up needed</div>
    <div class="row"><span class="dot"></span><span class="lbl">Needs Support</span>Missed urgent duties, accuracy or stress issues</div>
  </div>
</section>

<section class="sec reflect" style="left:622px;top:624px">
  <div class="sec-head">
    <svg class="icon" style="left:150px;top:-8px" width="28" height="32" viewBox="0 0 28 32"><rect x="2" y="3" width="20" height="27" fill="#fff" stroke="#2e9b5a" stroke-width="2"/><g stroke="#2e9b5a" stroke-width="1.5"><line x1="6" y1="10" x2="17" y2="10"/><line x1="6" y1="15" x2="15" y2="15"/><line x1="6" y1="20" x2="12" y2="20"/></g><path d="M12 25l12-15 3 2-12 15-4 1z" fill="#fff" stroke="#2e9b5a" stroke-width="1.5"/></svg>
    Daily Reflection</div>
  <div class="rows">
    <div class="line-row">What went well today ?<span class="fill"></span></div>
    <div class="line-row">Any issues or barriers to note ?<span class="fill"></span></div>
    <div class="line-row">Support needed from supervisor ?<span class="fill"></span></div>
  </div>
</section>

<section class="sec flags" style="left:622px;top:746px">
  <div class="sec-head">
    <svg width="20" height="19" viewBox="0 0 20 19" style="margin-right:12px"><path d="M10 0l3 6.5 7 .8-5.2 4.8 1.4 6.9L10 15.5 3.8 19l1.4-6.9L0 7.3l7-.8z" fill="#7a3f2a"/></svg>
    Stars &amp;
    <svg width="24" height="22" viewBox="0 0 24 22" style="margin:0 10px 0 8px"><path d="M2 2v20" stroke="#7a3f2a" stroke-width="2"/><path d="M3 2c5-3 9 3 20 0l-3 6 3 5c-10 3-15-3-20 0z" fill="#7a3f2a"/></svg>
    Flags (Supervisor Use Only)</div>
  <div class="rows">
    <div class="line-row"><svg width="14" height="14" viewBox="0 0 20 19"><path d="M10 0l3 6.5 7 .8-5.2 4.8 1.4 6.9L10 15.5 3.8 19l1.4-6.9L0 7.3l7-.8z" fill="#7a3f2a"/></svg>Excellence or above-and-beyond moments<span class="fill"></span></div>
    <div class="line-row"><svg width="16" height="14" viewBox="0 0 24 22"><path d="M2 2v20" stroke="#7a3f2a" stroke-width="2"/><path d="M3 2c5-3 9 3 20 0l-3 6 3 5c-10 3-15-3-20 0z" fill="#7a3f2a"/></svg>Concerns needing follow-up/coaching<span class="fill"></span></div>
  </div>
</section>

<section class="sec mgr" style="left:622px;top:837px">
  <div class="sec-head">
    <svg width="16" height="16" viewBox="0 0 16 16" style="margin-right:14px"><path d="M8 0l8 8-8 8-8-8z" fill="#fff"/></svg>
    Manager's Overall Rating</div>
  <div class="rows">
    <div class="line-row">Please rate overall performance on a 1-5 scale</div>
    <div class="line-row">Manager Overall Rating<span class="fill" style="flex:0 0 122px;margin-left:8px"></span></div>
  </div>
</section>

<div class="sign">
  <div class="s">Receptionist Sign.<span class="fill"></span></div>
  <div class="s">Supervisor Sign.<span class="fill"></span></div>
  <div class="s d">Date<span class="fill"></span></div>
</div>
</body>
</html>
```